VERIDAX Need a luxury modern business card designed.

Need a luxury modern business card designed. refer to the uploaded files for the company name and logo in the zip file under source files. i will making my descion on monday. so please send in before then so if we need to edit we will have the time. we have a trade show coming up and im on a deadline for printer.

Target Market(s)

high end clients

Contact Information for Business Card

Company nAme and logo. Calvin Ostrow Co-Founder / Project Manager Office # 416-555-0193 Cell # 416-555-0147 VERIDAX.CA Calvin@veridax.ca

Font styles to use
Other font styles liked:
• Modern

Requirements
Must have
• Company name and logo, contact info, using the black, gold and white color scheme.

```html
<!DOCTYPE html>
<html lang="en">
<head>
<meta charset="utf-8">
<title>VERIDAX Business Card</title>
<link href="https://fonts.googleapis.com/css2?family=Work+Sans:wght@300;400;600;700&display=swap" rel="stylesheet">
<style>
  :root {
    --stage: #3a302b;
    --card: #262627;
    --card-edge: #8f8550;
    --gold: #b3a56a;
    --white: #f4f4f2;
    --muted: #d9d9d6;
  }
  * { margin: 0; padding: 0; box-sizing: border-box; }
  html, body {
    width: 1200px; height: 847px; overflow: hidden;
    background: var(--stage);
    font-family: "Work Sans", Arial, sans-serif;
  }
  .canvas { position: relative; width: 1200px; height: 847px; }
  .card {
    position: absolute;
    width: 520px; height: 297px;
    background: var(--card);
    border: 2px solid var(--card-edge);
    border-radius: 3px;
    box-shadow: 0 10px 24px rgba(0,0,0,.35);
  }
  .card-front { left: 60px; top: 120px; }
  .card-back { left: 620px; top: 430px; }

  .wordmark {
    display: flex; align-items: center; gap: 10px;
    color: var(--white);
    font-weight: 300;
    letter-spacing: 6px;
  }
  .wordmark .mark-square {
    width: 12px; height: 12px; background: var(--gold);
  }
  .card-front .wordmark {
    position: absolute; right: 40px; bottom: 46px;
    font-size: 34px;
  }
  .card-back .wordmark {
    position: absolute; left: 34px; top: 128px;
    font-size: 28px;
  }
  .divider {
    position: absolute; left: 262px; top: 70px;
    width: 1px; height: 160px; background: var(--gold);
  }
  .contact {
    position: absolute; left: 284px; top: 72px;
    color: var(--white);
  }
  .contact .name {
    color: var(--gold); font-weight: 700;
    font-size: 17px; text-transform: uppercase; letter-spacing: .5px;
  }
  .contact .role { font-size: 12.5px; margin: 2px 0 12px; color: var(--muted); }
  .contact ul { list-style: none; }
  .contact li {
    display: flex; align-items: center; gap: 8px;
    font-size: 13.5px; line-height: 22px;
  }
  .contact svg { width: 12px; height: 12px; fill: var(--muted); flex: none; }
</style>
</head>
<body>
<div class="canvas">
  <section class="card card-front">
    <div class="wordmark"><span class="mark-square"></span>VERIDAX</div>
  </section>

  <section class="card card-back">
    <div class="wordmark"><span class="mark-square"></span>VERIDAX</div>
    <div class="divider"></div>
    <div class="contact">
      <p class="name">Calvin Ostrow</p>
      <p class="role">Co-Founder / Project Manager</p>
      <ul>
        <li>
          <svg viewBox="0 0 24 24"><path d="M6.6 10.8a15 15 0 0 0 6.6 6.6l2.2-2.2a1 1 0 0 1 1-.25 11.4 11.4 0 0 0 3.6.57 1 1 0 0 1 1 1V20a1 1 0 0 1-1 1A17 17 0 0 1 3 4a1 1 0 0 1 1-1h3.5a1 1 0 0 1 1 1c0 1.25.2 2.45.57 3.57a1 1 0 0 1-.25 1z"/></svg>
          416-555-0193
        </li>
        <li>
          <svg viewBox="0 0 24 24"><path d="M7 1h10a2 2 0 0 1 2 2v18a2 2 0 0 1-2 2H7a2 2 0 0 1-2-2V3a2 2 0 0 1 2-2zm0 3v14h10V4zm5 15.5a1 1 0 1 0 0 2 1 1 0 0 0 0-2z"/></svg>
          416-555-0147
        </li>
        <li>
          <svg viewBox="0 0 24 24"><path d="M2 5h20v14H2zm2 2v.5l8 5 8-5V7zm0 2.8V17h16V9.8l-8 5z"/></svg>
          Calvin@veridax.ca
        </li>
        <li>
          <svg viewBox="0 0 24 24"><path d="M12 2a10 10 0 1 0 0 20 10 10 0 0 0 0-20zm6.9 6h-2.9a15 15 0 0 0-1.4-3.6A8 8 0 0 1 18.9 8zM12 4c.8 1.2 1.5 2.5 1.9 4h-3.8c.4-1.5 1.1-2.8 1.9-4zM4.3 14a8 8 0 0 1 0-4h3.4a16 16 0 0 0 0 4zm.8 2h2.9c.3 1.3.8 2.5 1.4 3.6A8 8 0 0 1 5.1 16zM8 8H5.1a8 8 0 0 1 4.3-3.6C8.8 5.5 8.3 6.7 8 8zm4 12c-.8-1.2-1.5-2.5-1.9-4h3.8c-.4 1.5-1.1 2.8-1.9 4zm2.3-6H9.7a14 14 0 0 1 0-4h4.6a14 14 0 0 1 0 4zm.3 5.6c.6-1.1 1.1-2.3 1.4-3.6h2.9a8 8 0 0 1-4.3 3.6zm1.7-5.6a16 16 0 0 0 0-4h3.4a8 8 0 0 1 0 4z"/></svg>
          VERIDAX.CA
        </li>
      </ul>
    </div>
  </section>
</div>
</body>
</html>
```